BRINTEX Hardware needs a Flyer Designed

We need a flyer designed for a marketing strategy that is to be launched by BRINTEX. As it is for our hardware division, our logo should go unto the flyer. We are offering to our customers financing on items from $5000 up to $35000. Here are some key words that you may want to include; "building or revovating? you pick the job we've got the financing." The flyer should reflect some sort of home construction and should be very attractive and vibrant. On the flyer it should also state that it's "hassle-free" and; "no down payment", "no collateral", "affordable monthly payments".

Must Haves [en ]: The companies logo. Also it must state the address of the company and contact info which is; 47 Fellowby Lane Penal, Trinidad. Tel: 868-47-BRINTEX. Email must also be listed: info@brintexgroup.example.

Nice To Haves [en ]: Good quality graphics. something that is captivating and that will hold the attention of our audience.

Should Not Haves [en ]: Should not be too busy.

Requirements
Must have
• The companies logo. Also it must state the address of the company and contact info which is; 47 Fellowby Lane Penal, Trinidad. Tel: 868-47-BRINTEX. Email must also be listed: info@brintexgroup.example.
Nice to have
• Good quality graphics. something that is captivating and that will hold the attention of our audience.
Should not have
• Should not be too busy.

```html
<!DOCTYPE html>
<html lang="en">
<head>
<meta charset="utf-8">
<title>BRINTEX Hardware – Financing Flyer</title>
<link rel="stylesheet" href="https://fonts.googleapis.com/css2?family=Saira+Semi+Condensed:wght@600;700;800&family=Lato:wght@400;700&display=swap">
<style>
  :root{
    --navy:#1d2d5c;
    --red:#dc1f3f;
    --ink:#1f2226;
    --paper:#f1f1f3;
    --paper-light:#fafafa;
    --stage:#ececec;
    --grey-stripe:#8d8f94;
    --white:#ffffff;
  }
  *{margin:0;padding:0;box-sizing:border-box}
  html,body{width:1200px;height:1200px;overflow:hidden;background:var(--stage)}
  .canvas{position:relative;width:1200px;height:1200px}
  .flyer{
    position:absolute;left:20px;top:152px;width:1390px;height:1073px;
    transform:scale(0.8345);transform-origin:0 0;
    background:linear-gradient(180deg,var(--paper) 0%,var(--paper-light) 100%);
    overflow:hidden;
    font-family:"Saira Semi Condensed",sans-serif;
  }
  .shapes{position:absolute;inset:0}
  .brand{position:absolute;left:68px;top:62px;width:410px}
  .brand-name{display:flex;align-items:center;gap:14px}
  .brand-dot{width:34px;height:34px;border-radius:50%;background:var(--red)}
  .brand-word{font-weight:800;font-size:88px;line-height:1;color:var(--navy);letter-spacing:2px}
  .brand-legal{margin-top:6px;text-align:right;font-weight:700;font-size:15px;color:var(--navy);letter-spacing:.5px;border-bottom:3px solid var(--red);padding-bottom:2px}
  .brand-group{margin-top:8px;border-top:1.5px solid var(--navy);padding-top:4px;text-align:center;font-family:"Lato",sans-serif;font-size:17px;color:#3a3d45;letter-spacing:1px}
  .headline{position:absolute;left:45px;top:270px;text-transform:uppercase;font-weight:700;line-height:1}
  .headline .line-navy{color:var(--navy);font-size:36px;letter-spacing:.5px}
  .headline .line-red{color:var(--red);font-size:54px;margin:14px 0 12px;letter-spacing:1px}
  .offer{position:absolute;left:0;top:480px;width:620px;text-align:center;color:var(--white);font-weight:700;line-height:1}
  .offer .offer-title{font-size:64px}
  .offer .offer-range{font-size:46px;margin-top:22px}
  .benefits{position:absolute;left:75px;top:695px;list-style:none}
  .benefits li{display:flex;align-items:center;height:68px;font-size:33px;font-weight:700;color:var(--ink)}
  .benefits svg{width:44px;height:44px;margin-right:20px;flex:none}
  .website{position:absolute;left:60px;top:1003px;width:600px;text-align:center;font-family:"Lato",sans-serif;font-size:30px;letter-spacing:9px;color:var(--navy)}
  .contact{position:absolute;left:930px;top:862px;list-style:none;font-family:"Lato",sans-serif;color:var(--white);font-size:25px}
  .contact li{display:flex;align-items:center;height:35px}
  .contact svg{width:26px;height:26px;margin-right:22px;flex:none}
  .social{position:absolute;left:1038px;top:984px;display:flex;gap:18px}
  .social span{width:46px;height:46px;border:2px solid var(--white);border-radius:50%}
</style>
</head>
<body>
<main class="canvas">
  <section class="flyer">
    <svg class="shapes" viewBox="0 0 1390 1073" width="1390" height="1073">
      <defs>
        <linearGradient id="photoTone" x1="0" y1="0" x2="0" y2="1">
          <stop offset="0" stop-color="#5f93d8"/>
          <stop offset="0.35" stop-color="#c9b48e"/>
          <stop offset="1" stop-color="#9c8667"/>
        </linearGradient>
        <linearGradient id="stripeGrey" x1="0" y1="0" x2="1" y2="1">
          <stop offset="0" stop-color="#5c5f66"/>
          <stop offset="0.5" stop-color="#c4c6ca"/>
          <stop offset="1" stop-color="#6b6e75"/>
        </linearGradient>
      </defs>
      <polygon role="img" aria-label="Photo: house under construction with stone facade, scaffolding and blue sky" points="500,0 1390,0 1390,826 835,826" fill="url(#photoTone)"/>
      <polygon class="contact-panel" points="835,826 1390,826 1390,1073 935,1073" fill="var(--navy)"/>
      <polygon class="stripe-grey" points="465,0 485,0 920,1073 900,1073" fill="url(#stripeGrey)"/>
      <polygon class="stripe-red" points="485,0 500,0 935,1073 920,1073" fill="var(--red)"/>
      <polygon class="offer-band" points="0,468 608,468 677,646 0,646" fill="var(--red)"/>
      <polygon class="footer-rule" points="0,983 866,983 870,993 0,993" fill="var(--navy)"/>
      <polygon class="footer-band" points="0,993 870,993 903,1073 0,1073" fill="var(--white)"/>
    </svg>

    <header class="brand">
      <div class="brand-name"><span class="brand-dot"></span><span class="brand-word">BRINTEX</span></div>
      <div class="brand-legal">Brintex Trading Company Limited</div>
      <div class="brand-group">GROUP OF COMPANIES</div>
    </header>

    <h1 class="headline">
      <div class="line-navy">Building or Revovating?</div>
      <div class="line-red">You Pick the Job</div>
      <div class="line-navy">We’ve Got the Financing</div>
    </h1>

    <div class="offer">
      <div class="offer-title">Items From</div>
      <div class="offer-range">$ 5000 up to $ 35000</div>
    </div>

    <ul class="benefits">
      <li><svg viewBox="0 0 44 44"><circle cx="22" cy="22" r="19" fill="var(--red)"/><path d="M13 22l6 6 12-12" fill="none" stroke="#fff" stroke-width="3.5" stroke-linecap="round" stroke-linejoin="round"/></svg>Hassle-Free</li>
      <li><svg viewBox="0 0 44 44"><circle cx="22" cy="22" r="18" fill="none" stroke="var(--red)" stroke-width="3"/><line x1="9" y1="9" x2="35" y2="35" stroke="var(--red)" stroke-width="3"/></svg>No Collateral</li>
      <li><svg viewBox="0 0 44 44"><circle cx="22" cy="22" r="18" fill="none" stroke="var(--red)" stroke-width="3"/><path d="M15 12l14 20M29 12L15 32" stroke="var(--red)" stroke-width="3"/></svg>No Down Payment</li>
      <li><svg viewBox="0 0 44 44"><circle cx="22" cy="22" r="18" fill="none" stroke="var(--red)" stroke-width="2.5"/><rect x="12" y="14" width="16" height="14" rx="1.5" fill="none" stroke="var(--red)" stroke-width="2"/><line x1="12" y1="18" x2="28" y2="18" stroke="var(--red)" stroke-width="2"/><text x="29" y="32" font-size="10" font-family="Lato,sans-serif" font-weight="700" fill="var(--red)">$</text></svg>Affordable Monthly Payments</li>
    </ul>

    <div class="website">www.brintexgroup.example</div>

    <ul class="contact">
      <li><svg viewBox="0 0 26 26"><path d="M13 2a8 8 0 0 0-8 8c0 6 8 14 8 14s8-8 8-14a8 8 0 0 0-8-8z" fill="none" stroke="#fff" stroke-width="2.2"/><circle cx="13" cy="10" r="3" fill="#fff"/></svg>47 Fellowby Lane Penal, Trinidad</li>
      <li><svg viewBox="0 0 26 26"><path d="M3 9c0-3 4-5 10-5s10 2 10 5v2h-5V8H8v3H3z" fill="#fff"/><rect x="5" y="13" width="16" height="10" rx="2" fill="#fff"/><circle cx="13" cy="18" r="2.5" fill="var(--navy)"/></svg>868-47-BRINTEX</li>
      <li><svg viewBox="0 0 26 26"><rect x="3" y="7" width="20" height="15" fill="none" stroke="#fff" stroke-width="1.8"/><path d="M3 7l10 8 10-8" fill="none" stroke="#fff" stroke-width="1.8"/></svg>info@brintexgroup.example</li>
    </ul>

    <div class="social"><span></span><span></span><span></span></div>
  </section>
</main>
</body>
</html>
```